WeighTheMatterClearly.net, a blog on economics and social issues, needs a facelift.

Make my blog website more attractive and functional.
It needs a cover image. The purpose of the blog is to sort out errors the public discourse on current topics that affect timeless issues. It is to correct erroneous conclusions on public issues caused by ignoring relevant facts, misunderstandings of the facts upon which they base conclusions, and/or misanalysis of the facts. The topics vary widely.

I have in mind some kind of transition from an out of focus area to a focused area. At one time I used the attached image, but it gave no hint of a transition from a lack of clarity to clarity. I am wide open to other approaches to conveying that idea.

A particular improvement would be making the Subscribe button to be easier to find,

Target Market(s)

People interested in how timeless economic, social, constitutional, political philosophy, and governance ideals apply to current affairs.

Logo Text

While I would not rule it out, I don't have in mind that the logo will be different from the cover image. The essence of the blog is mostly captured by its name, Weigh the Matter Clearly.

Requirements
Must have
• Cover image. Webpages that are nice looking and appropriate to the seriousness of the blog.

FOLLOW and SHARE buttons in easily found places.
Nice to have
• Instructions as to how to transfer/set up what I receive from the designer to the WordPress website.

Suggestions on Fonts.

Suggested changes to the pages.

BTW: I had no help setting up the current page.
Should not have
• Anything that hints that I am interested in or facilitiates the receipt of money from followers.

```html
<!DOCTYPE html>
<html lang="en">
<head>
<meta charset="utf-8">
<title>Weigh the Matter Clearly</title>
<link rel="stylesheet" href="https://fonts.googleapis.com/css2?family=Merriweather:wght@400;700&family=Montserrat:wght@400;500;600;700;800;900&display=swap">
<style>
:root{
  --red:#f5393f;
  --ink:#1f1f1f;
  --muted:#8a8a8a;
  --body:#3a3a3a;
  --line:#d9d9d9;
  --white:#ffffff;
  --photo-red:#d9666a;
}
*{box-sizing:border-box;margin:0;padding:0}
html,body{width:1200px;height:2780px;overflow:hidden;background:var(--white)}
body{font-family:'Montserrat',sans-serif;color:var(--ink);position:relative}
.page{position:relative;width:1200px;height:2780px;overflow:hidden}
.abs{position:absolute}

/* header */
.menu-toggle{left:92px;top:53px;width:22px;height:16px}
.menu-toggle span{display:block;height:2px;background:var(--ink);margin-bottom:5px}
.site-title{left:0;width:1200px;top:31px;text-align:center;font-family:'Merriweather',serif;font-weight:700;font-size:35px;color:var(--ink);letter-spacing:.2px;z-index:1}
.site-title .mark{position:relative;display:inline-block}
.site-title .mark::after{content:"";position:absolute;left:0;right:0;bottom:4px;height:5px;background:var(--red);z-index:-1}
.btn{display:flex;align-items:center;justify-content:center;width:138px;height:33px;font-weight:700;font-size:12px;text-decoration:none}
.btn-solid{background:var(--red);color:var(--white)}
.btn-outline{border:1px solid var(--red);color:var(--red);background:var(--white)}
.header-subscribe{left:970px;top:43px}

/* hero */
.hero{left:0;top:110px;width:1200px;height:632px;border:1px solid #222;
  background:radial-gradient(ellipse 60% 40% at 50% 55%,#4e6a72 0%,transparent 70%),
  linear-gradient(180deg,#2b3f48 0%,#3d5560 35%,#2a3a42 65%,#1a2226 100%)}
.hero-line{position:absolute;left:0;width:1200px;text-align:center;color:var(--white);font-weight:900;font-size:62px;letter-spacing:-1px;line-height:1}
.hero-line em{font-style:normal;color:var(--red)}
.hero-social{left:1090px;top:705px;display:flex;gap:8px}
.social-label{font-size:9px;font-weight:600;color:var(--white)}

/* posts */
.post{left:94px;width:676px;height:348px;background:var(--white)}
.post.featured{box-shadow:0 2px 10px rgba(0,0,0,.12)}
.post-thumb{position:absolute;left:0;top:0;width:206px;height:348px;background:linear-gradient(160deg,#e6877f 0%,var(--photo-red) 45%,#b84b52 100%)}
.post-rule{position:absolute;left:178px;top:57px;width:67px;height:1px;background:#333}
.post-title{position:absolute;left:251px;top:39px;width:400px;font-family:'Merriweather',serif;font-weight:700;font-size:25px;line-height:33px;color:var(--ink)}
.post-meta{position:absolute;left:251px;top:152px;font-size:12px;color:var(--muted);letter-spacing:.3px}
.post-excerpt{position:absolute;left:251px;top:192px;width:400px;font-size:14.5px;line-height:23px;color:var(--body)}
.post .btn{position:absolute;left:509px;top:284px}

/* author */
.author{left:818px;top:686px;width:252px;height:348px;background:var(--white);box-shadow:0 2px 10px rgba(0,0,0,.12)}
.author-band{position:absolute;left:0;top:0;width:252px;height:130px;background:var(--red)}
.author-photo{position:absolute;left:63px;top:28px;width:126px;height:126px;background:linear-gradient(180deg,#4a4a4a,#1c1c1c)}
.author-name{position:absolute;left:0;width:262px;top:169px;text-align:center;font-size:12px;font-weight:500;letter-spacing:.5px}
.author-role{position:absolute;left:0;width:252px;top:193px;text-align:center;font-size:14px;color:var(--body)}
.author .btn{position:absolute;left:57px}

/* sidebar */
.widget-title{font-family:'Merriweather',serif;font-weight:700;font-size:16px;color:var(--ink);position:absolute;display:inline-block;z-index:1}
.widget-title::after{content:"";position:absolute;left:0;right:0;bottom:1px;height:3px;background:var(--red);z-index:-1}
.top-list{left:830px;top:1140px;width:228px;list-style:none}
.top-list li{padding:8px 0 14px 24px;border-bottom:1px solid var(--line);font-size:12px;line-height:19px;color:var(--ink);font-weight:500}
.top-list li:last-child{border-bottom:none}
.subscribe-text{left:854px;top:1578px;width:230px;font-size:12px;line-height:19px;font-weight:500}
.email-field{left:855px;top:1671px;width:216px;height:33px;border:1px solid #555;display:flex;align-items:center;justify-content:center;font-size:12px;color:var(--muted)}

/* footer */
.footer{left:0;top:2703px;width:1200px;height:77px;background:var(--red);color:var(--white)}
.footer-copy{position:absolute;left:92px;top:32px;font-size:11px}
.footer-nav a{color:var(--white);text-decoration:none;position:absolute;top:31px;font-size:15px;white-space:nowrap}
.footer-social{position:absolute;left:1022px;top:34px;display:flex;gap:8px}
</style>
</head>
<body>
<div class="page">

  <header>
    <div class="abs menu-toggle" aria-label="Menu"><span></span><span></span><span></span></div>
    <div class="abs site-title">Weigh the <span class="mark">Matter Clearly</span></div>
    <a class="abs btn btn-solid header-subscribe" href="#">Subscribe</a>
  </header>

  <section class="abs hero" role="img" aria-label="Cover photo: a city at night seen blurred, coming into focus through a pair of eyeglasses">
    <div class="hero-line" style="top:200px">A place to <em>seek clarity</em> on</div>
    <div class="hero-line" style="top:276px">timeless issues and issues</div>
    <div class="hero-line" style="top:353px">of the day.</div>
  </section>
  <div class="abs hero-social">
    <span class="social-label">Follow</span>
    <span class="social-label">Share</span>
    <span class="social-label">Feed</span>
  </div>

  <main>
    <article class="abs post featured" style="top:686px">
      <div class="post-thumb" role="img" aria-label="Photo of a child at a march holding an ‘Enough is Enough’ sign, red tint"></div>
      <div class="post-rule"></div>
      <h2 class="post-title">What’s Going On? – Part VIII Equal Lives Do Matter, ELM Misdirection</h2>
      <p class="post-meta">POSTED ON OCTOBER 8, 2020 BY MARTIN HALE</p>
      <p class="post-excerpt">Because equal lives do matter so much, a movement<br>to deal with the many valid grievances is necessary<br>and overdue.</p>
      <a class="btn btn-outline" href="#">Read More</a>
    </article>

    <article class="abs post" style="top:1081px">
      <div class="post-thumb" role="img" aria-label="Photo of a child at a march holding an ‘Enough is Enough’ sign, red tint"></div>
      <div class="post-rule"></div>
      <h2 class="post-title">What’s Going On? – Part VIII Equal Lives Do Matter, ELM Misdirection</h2>
      <p class="post-meta">POSTED ON OCTOBER 8, 2020 BY MARTIN HALE</p>
      <p class="post-excerpt">Because equal lives do matter so much, a movement<br>to deal with the many valid grievances is necessary<br>and overdue.</p>
      <a class="btn btn-outline" href="#">Read More</a>
    </article>

    <article class="abs post" style="top:1476px">
      <div class="post-thumb" role="img" aria-label="Photo of a child at a march holding an ‘Enough is Enough’ sign, red tint"></div>
      <div class="post-rule"></div>
      <h2 class="post-title">What’s Going On? – Part VIII Equal Lives Do Matter, ELM Misdirection</h2>
      <p class="post-meta">POSTED ON OCTOBER 8, 2020 BY MARTIN HALE</p>
      <p class="post-excerpt">Because equal lives do matter so much, a movement<br>to deal with the many valid grievances is necessary<br>and overdue.</p>
      <a class="btn btn-outline" href="#">Read More</a>
    </article>

    <article class="abs post" style="top:1869px">
      <div class="post-thumb" role="img" aria-label="Photo of a child at a march holding an ‘Enough is Enough’ sign, red tint"></div>
      <div class="post-rule"></div>
      <h2 class="post-title">What’s Going On? – Part VIII Equal Lives Do Matter, ELM Misdirection</h2>
      <p class="post-meta">POSTED ON OCTOBER 8, 2020 BY MARTIN HALE</p>
      <p class="post-excerpt">Because equal lives do matter so much, a movement<br>to deal with the many valid grievances is necessary<br>and overdue.</p>
      <a class="btn btn-outline" href="#">Read More</a>
    </article>

    <article class="abs post" style="top:2264px">
      <div class="post-thumb" role="img" aria-label="Photo of a child at a march holding an ‘Enough is Enough’ sign, red tint"></div>
      <div class="post-rule"></div>
      <h2 class="post-title">What’s Going On? – Part VIII Equal Lives Do Matter, ELM Misdirection</h2>
      <p class="post-meta">POSTED ON OCTOBER 8, 2020 BY MARTIN HALE</p>
      <p class="post-excerpt">Because equal lives do matter so much, a movement<br>to deal with the many valid grievances is necessary<br>and overdue.</p>
      <a class="btn btn-outline" href="#">Read More</a>
    </article>
  </main>

  <aside>
    <div class="abs author">
      <div class="author-band" role="img" aria-label="Red textured pattern band"></div>
      <div class="author-photo" role="img" aria-label="Portrait photo of the author"></div>
      <div class="author-name">MARTIN HALE</div>
      <div class="author-role">Blogger - Journalist</div>
      <a class="btn btn-outline" href="#" style="top:243px">All Articles</a>
      <a class="btn btn-solid" href="#" style="top:288px">Subscribe</a>
    </div>

    <h3 class="widget-title" style="left:854px;top:1103px">Top Post</h3>
    <ul class="abs top-list">
      <li>The Truth Is Still Hard For The<br>Daily Ledger.</li>
      <li>What’s Going On? – Part VII<br>Equal Lives Do Matter,<br>Dashed Hopes</li>
      <li>The Attention Trap – A Review</li>
      <li>What’s Going On? – Part VI<br>Equal Lives Do Matter, The<br>Stereotyping Problem</li>
      <li>What’s Going On? – Part V<br>Equal Lives Do Matter, Unfair<br>Discriminatory Structures</li>
    </ul>

    <h3 class="widget-title" style="left:854px;top:1546px">Subscribe to Blog</h3>
    <p class="abs subscribe-text">Enter your email address to<br>subscribe to this blog and receive<br>notifications of new posts by<br>email.</p>
    <div class="abs email-field">Enter your Email</div>
    <a class="abs btn btn-solid" href="#" style="left:855px;top:1715px;width:216px">Subscribe</a>
  </aside>

  <footer class="abs footer">
    <div class="footer-copy">© 2020 by Weigh the Matter Clearly. All rights reserved.</div>
    <nav class="footer-nav">
      <a href="#" style="left:601px">Home</a>
      <a href="#" style="left:679px">About</a>
      <a href="#" style="left:757px">Contact</a>
      <a href="#" style="left:850px">Privacy Policy</a>
    </nav>
    <div class="footer-social">
      <span class="social-label">Follow</span>
      <span class="social-label">Share</span>
      <span class="social-label">Feed</span>
    </div>
  </footer>

</div>
</body>
</html>
```